Brackenfield Bike Tours Van Wrap

We have a large van that needs a partial wrap, using photos or drawings and our logo/word mark.  Here is our website https://www.brackenfieldbiketours.com/
We need our logo, website and phone number 555 014 2287 as part of the wrap.  Looking for the wrap to slope from the back top corner down towards the front door.  Covering the back 2 windows on the side and covering the rear windows.
See the van in the link below 2018 Brava K 270 MX Black.   An option is to use graphics on the side of the van and have phone number logo website on the front doors.  Please use your creative expertise.

Target Market(s)
Upscale techies in Seattle
Requirements
Must have
- Phone number, website and name of the company

Nice to have
- Creative use of our logo, feel free to take some license with our current logo.

```html
<!DOCTYPE html>
<html lang="en">
<head>
<meta charset="utf-8">
<title>Brackenfield Bike Tours – Van Wrap Panel</title>
<link rel="stylesheet" href="https://fonts.googleapis.com/css2?family=Arimo:wght@400;700&display=swap">
<style>
  :root {
    --wrap-orange: #ff8a00;
    --divider-black: #000000;
    --gap-white: #ffffff;
    --ink-black: #000000;
    --brand-white: #ffffff;
    --forest-dark: #3d3a14;
    --forest-green: #7f8f2a;
    --forest-gold: #d89a2a;
    --leaf-rust: #a8461a;
  }
  html, body {
    margin: 0;
    padding: 0;
    width: 1200px;
    height: 490px;
    overflow: hidden;
    background: var(--gap-white);
  }
  .wrap-panel {
    position: relative;
    width: 1200px;
    height: 490px;
    overflow: hidden;
    background: var(--gap-white);
    font-family: "Arimo", Arial, sans-serif;
  }
  .trail-photo {
    position: absolute;
    left: 0;
    top: 0;
    width: 727px;
    height: 490px;
    background:
      linear-gradient(180deg, rgba(0,0,0,0) 55%, var(--leaf-rust) 100%),
      radial-gradient(ellipse at 55% 15%, #f4e7a8 0%, rgba(244,231,168,0) 35%),
      linear-gradient(90deg, var(--forest-dark) 0%, var(--forest-green) 35%, var(--forest-gold) 65%, var(--forest-dark) 100%);
  }
  .divider-band {
    position: absolute;
    left: 733px;
    top: 0;
    width: 24px;
    height: 490px;
    background: var(--divider-black);
  }
  .contact-panel {
    position: absolute;
    left: 761px;
    top: 0;
    width: 439px;
    height: 490px;
    background: var(--wrap-orange);
  }
  .brand-name {
    position: absolute;
    right: 22px;
    top: 222px;
    margin: 0;
    text-align: right;
    color: var(--brand-white);
    font-weight: 400;
    line-height: 1;
  }
  .brand-name .brand-main {
    display: block;
    font-size: 46px;
    letter-spacing: 0.5px;
  }
  .brand-name .brand-sub {
    display: block;
    margin-top: 6px;
    font-size: 15px;
    letter-spacing: 2.4px;
  }
  .website {
    position: absolute;
    right: 27px;
    top: 312px;
    margin: 0;
    color: var(--ink-black);
    font-weight: 700;
    font-size: 21px;
  }
  .phone {
    position: absolute;
    right: 21px;
    top: 350px;
    margin: 0;
    color: var(--ink-black);
    font-weight: 700;
    font-size: 44px;
    white-space: nowrap;
  }
</style>
</head>
<body>
  <main class="wrap-panel">
    <div class="trail-photo" role="img" aria-label="Photo: two mountain bikers riding a leaf-covered trail through a tall autumn forest"></div>
    <div class="divider-band"></div>
    <section class="contact-panel">
      <h1 class="brand-name">
        <span class="brand-main">brackenfield</span>
        <span class="brand-sub">BIKE TOURS</span>
      </h1>
      <p class="website">www.brackenfieldbiketours.com</p>
      <p class="phone">call : 555 014 2287</p>
    </section>
  </main>
</body>
</html>
```